Cowboy Ned
Cowboy Ned -
Professional
"Cowboy Ned" Hollins, Broker/Owner
Cowboy Ned Realty, LLC
4382 W Juniper Ridge Ln Gilbert, AZ 85297 (Address to be in smaller letters so as not to stand out)
Ned@CowboyNedRealty.example
www.CowboyNedRealty.example
Blog: http://housetalkhub.example/blogs/cowboyned Logo will be uploaded and should be on the front of the card. It may take up the whole front, or the front may include my phone and fax number. KTM, uDOM, FHLS, VOT Those designations above are to be added under my name.
The back will have possibly my head shot plus the contact information, web sites, etc and a couple of required plain square badge logos scaled very small so as to hardly be noticeable.

```html
<!DOCTYPE html>
<html lang="en">
<head>
<meta charset="utf-8">
<title>Cowboy Ned Hollins – Business Card</title>
<link rel="stylesheet" href="https://fonts.googleapis.com/css2?family=Arimo:wght@400;700&display=swap">
<style>
  :root {
    --blue-deep: #0d3f86;
    --blue-mid: #1a5cab;
    --blue-light: #3f86d0;
    --white: #ffffff;
    --ink-blue: #1d5fae;
    --badge: #2a3a55;
    --photo-top: #6f7f92;
    --photo-bottom: #2b2f3a;
  }
  html, body {
    margin: 0;
    padding: 0;
    width: 1200px;
    height: 739px;
    overflow: hidden;
    background: var(--white);
  }
  .card {
    position: relative;
    width: 1200px;
    height: 739px;
    overflow: hidden;
    font-family: "Arimo", Arial, sans-serif;
    color: var(--white);
    background: linear-gradient(160deg, var(--blue-deep) 0%, var(--blue-mid) 55%, var(--blue-light) 100%);
  }
  .card__wave {
    position: absolute;
    left: 0;
    top: 0;
    width: 1200px;
    height: 739px;
  }
  .agent-name {
    position: absolute;
    left: 70px;
    top: 66px;
    margin: 0;
    font-weight: 400;
    font-size: 56px;
    line-height: 1;
    letter-spacing: 0.5px;
  }
  .agent-name__role {
    font-size: 43px;
  }
  .designations {
    position: absolute;
    left: 72px;
    top: 152px;
    margin: 0;
    font-size: 38px;
    line-height: 1;
  }
  .brokerage {
    position: absolute;
    right: 34px;
    top: 154px;
    margin: 0;
    display: flex;
    align-items: center;
    gap: 14px;
    font-size: 32px;
    font-weight: 400;
    line-height: 1;
  }
  .brokerage__mark {
    width: 26px;
    height: 26px;
    background: var(--white);
  }
  .headshot {
    position: absolute;
    left: 162px;
    top: 250px;
    width: 222px;
    height: 284px;
    box-sizing: border-box;
    border: 5px solid var(--white);
    background: linear-gradient(180deg, var(--photo-top) 0%, var(--photo-bottom) 100%);
  }
  .contact {
    position: absolute;
    right: 34px;
    top: 256px;
    margin: 0;
    text-align: right;
    font-style: normal;
    font-size: 38px;
    line-height: 53px;
  }
  .contact__address {
    display: block;
    font-size: 27px;
    line-height: 36px;
    margin-bottom: 6px;
  }
  .blog {
    position: absolute;
    left: 62px;
    top: 682px;
    margin: 0;
    font-size: 32px;
    line-height: 1;
    color: var(--ink-blue);
  }
  .badge {
    position: absolute;
    top: 622px;
    width: 62px;
    height: 68px;
    background: var(--badge);
  }
  .badge--housing { left: 948px; }
  .badge--association { left: 1050px; background: var(--ink-blue); }
</style>
</head>
<body>
  <div class="card">
    <svg class="card__wave" viewBox="0 0 1200 739" aria-hidden="true">
      <path d="M0,650 C320,668 760,640 1200,548" fill="none" stroke="var(--blue-light)" stroke-width="10"/>
      <path d="M0,656 C320,674 760,646 1200,554 L1200,739 L0,739 Z" fill="var(--white)"/>
    </svg>

    <h1 class="agent-name">Cowboy Ned Hollins<span class="agent-name__role">, Broker/Owner</span></h1>
    <p class="designations">KTM, uDOM, FHLS, VOT</p>

    <p class="brokerage"><span class="brokerage__mark" aria-hidden="true"></span>Cowboy Ned Realty, LLC</p>

    <div class="headshot" role="img" aria-label="Head shot of Cowboy Ned Hollins"></div>

    <address class="contact">
      <span class="contact__address">4382 W Juniper Ridge Ln<br>Gilbert, AZ 85297</span>
      CELL (480) 555 0147<br>
      FAX (480) 555 0192<br>
      E-MAIL Ned@CowboyNedRealty.example<br>
      www.CowboyNedRealty.example
    </address>

    <p class="blog">Blog: http://housetalkhub.example/blogs/cowboyned</p>

    <div class="badge badge--housing" role="img" aria-label="Fair housing badge"></div>
    <div class="badge badge--association" role="img" aria-label="Association membership badge"></div>
  </div>
</body>
</html>
```